Business Card Design

We need a business card designed to portray the message that we are wedding and event stylists. We set up garden ceremonies and style wedding reception venues with chair covers and sashes, backdrops and draping's, wishing wells, tealight holders, table centerpieces. We also style corporate functions - Christmas parties, gala dinners, school formals, award nights. The colour of our uniforms are black and hot pink, if these colours could be incorporated. We would like to be able to use this design for letterhead, flyers and postcards etc. We would like the design to portray a professional, classic image that would relate to both spectrums of our business, weddings and corporate events. If you could develop a logo to incorporate would be great

Target Market(s)

brides, corporate compaines

Industry/Entity Type

Wedding

Contact Information for Business Card

Velvet Aisle & Function Rentals
Phone: 0413 586 190 Email:vaafr@quokkamail.com
Web: www.velvetaisleandfunctions.com.au

Requirements
Must have
• Must include that we set up for weddings, engagements, birthdays, anniversaries, corporate functions, school formals, any occasion.

```html
<!DOCTYPE html>
<html lang="en">
<head>
<meta charset="utf-8">
<title>Velvet Aisle &amp; Function Rentals — Business Card</title>
<link href="https://fonts.googleapis.com/css2?family=EB+Garamond:wght@400&display=swap" rel="stylesheet">
<style>
  :root {
    --card-black: #070707;
    --lattice-black: #171717;
    --scroll-gold: #b9b230;
    --scroll-gold-deep: #7a761f;
    --panel-yellow: #f6ec45;
    --panel-edge: #c9bb5a;
    --name-ink: #111111;
    --label-gold: #f2dc72;
    --text-white: #f4f1e6;
  }
  html, body {
    margin: 0;
    padding: 0;
    width: 1200px;
    height: 741px;
    overflow: hidden;
    background: var(--card-black);
  }
  .card {
    position: relative;
    width: 1200px;
    height: 741px;
    overflow: hidden;
    background: var(--card-black);
    font-family: "EB Garamond", Georgia, serif;
  }
  .lattice {
    position: absolute;
    inset: 0;
    background: radial-gradient(ellipse at center, var(--lattice-black) 0%, var(--card-black) 80%);
  }
  .scrollwork {
    position: absolute;
    left: 0;
    width: 1200px;
  }
  .scrollwork--top {
    top: 0;
    height: 215px;
    background: linear-gradient(to bottom, var(--scroll-gold-deep) 0%, rgba(122,118,31,0.6) 45%, rgba(7,7,7,0) 100%);
  }
  .scrollwork--bottom {
    bottom: 0;
    height: 200px;
    background: linear-gradient(to top, var(--scroll-gold-deep) 0%, rgba(122,118,31,0.6) 50%, rgba(7,7,7,0) 100%);
  }
  .brand {
    position: absolute;
    left: 389px;
    top: 229px;
    width: 387px;
    height: 281px;
    box-sizing: border-box;
    background: var(--panel-yellow);
    border: 3px solid var(--panel-edge);
    border-radius: 18px;
    display: flex;
    flex-direction: column;
    align-items: center;
    justify-content: center;
    text-align: center;
    color: var(--name-ink);
    font-weight: 400;
    font-size: 46px;
    line-height: 1.2;
  }
  .contact {
    position: absolute;
    margin: 0;
    font-size: 21px;
    line-height: 28px;
    color: var(--text-white);
    white-space: nowrap;
  }
  .contact__label { color: var(--label-gold); }
  .contact--web { left: 350px; top: 516px; }
  .contact--phone { left: 859px; top: 516px; }
  .contact--email { left: 859px; top: 543px; }
  .occasions {
    position: absolute;
    left: 0;
    top: 588px;
    width: 1200px;
    margin: 0;
    text-align: center;
    font-size: 19px;
    line-height: 26px;
    letter-spacing: 0.5px;
    color: var(--label-gold);
    white-space: nowrap;
  }
</style>
</head>
<body>
  <main class="card">
    <div class="lattice" role="img" aria-label="Dark black lattice pattern background"></div>
    <div class="scrollwork scrollwork--top" role="img" aria-label="Gold floral scrollwork border along the top edge"></div>
    <div class="scrollwork scrollwork--bottom" role="img" aria-label="Gold floral scrollwork border along the bottom edge"></div>

    <div class="brand">
      <span>Velvet Aisle &amp;</span>
      <span>Function Rentals</span>
    </div>

    <p class="contact contact--web"><span class="contact__label">Web:</span> www.velvetaisleandfunctions.com.au</p>
    <p class="contact contact--phone"><span class="contact__label">Phone:</span> 0413 586 190</p>
    <p class="contact contact--email"><span class="contact__label">Email:</span>vaafr@quokkamail.com</p>

    <p class="occasions">Weddings · Engagements · Birthdays · Anniversaries · Corporate Functions · School Formals · Any Occasion</p>
  </main>
</body>
</html>
```